Buch-/eBook-Cover für Autobiografie
Das Disign von dem Cover hat mir auf Anhieb sehr gut gefallen. Das hat gleich "ins schwarze" getroffen. Die Kommunikation war effizient und zielgerichtet
Zielgruppe
Ich bin eine Privatperson und habe im Laufe der letzten Jahre mein Autobiografie geschrieben. Besser gesagt ist es ein autobiografischer Roman geworden. Ich plane dieses Buch meiner Frau und meinen Söhnen und deren Familien zu schenken. Darüber hinaus ist es aber auch geplant das Buch bei Veltaro zu veröffentlichen.
Aufgabenstellung
Auf dem Cover sollte neben meinem Namen Konrad(a) Pelzmann natürlich auch der Titel von dem Buch stehen. Ich habe dem Buch den Titel gegeben: 'Das Licht am Ufer'. Auf dem Backcover hatte ich mir eine kurze zusammenfassung vorgestellt, die ich auch beifüge. Ich hatte geplant, das sowohl auf dem Cover, wie auch auf dem Backcover Bilder von mir (u.a. als Baby) mit gestaltet werden. Aber das ist nur so eine Idee, ich bin da für Vorschläge offen
Das Design darf nicht zu überladen sein.

```html
<!DOCTYPE html>
<html lang="de">
<head>
<meta charset="utf-8">
<title>Das Licht am Ufer – Buchumschlag</title>
<link rel="stylesheet" href="https://fonts.googleapis.com/css2?family=Playfair+Display:wght@400&family=Archivo:wght@400;500&display=swap">
<style>
  :root {
    --paper: #ece5d4;
    --ink: #2f3742;
    --ink-soft: #6a655c;
    --frame: #ffffff;
  }
  * { margin: 0; padding: 0; box-sizing: border-box; }
  html, body { width: 1200px; height: 899px; overflow: hidden; background: var(--paper); }
  .wrap { position: relative; width: 1200px; height: 899px; background: var(--paper); overflow: hidden; }

  .texture-area {
    position: absolute; left: 0; top: 0; width: 560px; height: 300px;
    background: radial-gradient(ellipse at 45% 35%, rgba(60,58,55,.18), rgba(236,229,212,0) 70%);
  }

  .photo {
    position: absolute;
    background: var(--frame);
    padding: 12px;
    box-shadow: 0 3px 10px rgba(0,0,0,.22);
  }
  .photo .fill { width: 100%; height: 100%; }
  .photo--baby  { left: 42px;  top: 28px;  width: 238px; height: 246px; transform: rotate(-2deg); }
  .photo--baby .fill  { background: linear-gradient(160deg, #c9b9a4, #8f7f6d); }
  .photo--bike  { left: 292px; top: 20px;  width: 246px; height: 306px; transform: rotate(4deg); }
  .photo--bike .fill  { background: linear-gradient(170deg, #d8d5cf, #9a9893 70%, #6e6d6a); }
  .photo--woman { left: 32px;  top: 246px; width: 270px; height: 296px; transform: rotate(-4deg); }
  .photo--woman .fill { background: linear-gradient(150deg, #e0b57a, #a86a3e 55%, #6d7f96); }
  .photo--teen  { left: 232px; top: 312px; width: 290px; height: 300px; transform: rotate(3deg); }
  .photo--teen .fill  { background: linear-gradient(170deg, #7c7873, #4d4b49); }

  .front-title {
    position: absolute; left: 40px; top: 622px; width: 500px;
    font-family: "Playfair Display", serif; font-weight: 400;
    font-size: 78px; line-height: 80px; color: var(--ink);
    text-align: center; letter-spacing: 1px;
  }
  .front-author {
    position: absolute; left: 40px; top: 818px; width: 470px;
    font-family: "Archivo", sans-serif; font-weight: 500;
    font-size: 32px; letter-spacing: 1.5px; color: #111;
    text-align: center;
  }

  .spine-title, .spine-author {
    position: absolute; writing-mode: vertical-rl; color: var(--ink);
  }
  .spine-title {
    left: 574px; top: 74px;
    font-family: "Playfair Display", serif; font-size: 40px; letter-spacing: 2px;
  }
  .spine-author {
    left: 588px; top: 676px;
    font-family: "Archivo", sans-serif; font-size: 15px; letter-spacing: 0.3px; color: #222;
  }

  .blurb {
    position: absolute; left: 691px; width: 460px;
    font-family: "Playfair Display", serif; font-size: 15.5px; line-height: 21.4px;
    color: var(--ink-soft);
  }
  .blurb--main { top: 50px; }
  .blurb--closing { top: 458px; }

  .author-photo {
    position: absolute; left: 693px; top: 690px; width: 122px; height: 158px;
    background: linear-gradient(180deg, #8a8b8d, #3d3f43 55%, #1c1d20);
  }
  .code-box {
    position: absolute; left: 950px; top: 720px; width: 182px; height: 128px;
    background: #fff;
    font-family: "Archivo", sans-serif; font-size: 13px; color: #333;
    display: flex; align-items: flex-end; justify-content: center; padding-bottom: 8px;
  }
</style>
</head>
<body>
<div class="wrap">
  <div class="texture-area" role="img" aria-label="Dekorative dunkle Tintenflecken hinter den Fotos"></div>

  <div class="photo photo--baby"><div class="fill" role="img" aria-label="Foto: Baby im hellen Hemd"></div></div>
  <div class="photo photo--bike"><div class="fill" role="img" aria-label="Foto: Junge auf einem Fahrrad vor einer Hauswand"></div></div>
  <div class="photo photo--woman"><div class="fill" role="img" aria-label="Foto: lächelnde Frau mit rotbraunem Haar im Abendlicht"></div></div>
  <div class="photo photo--teen"><div class="fill" role="img" aria-label="Foto: junge Frau mit Mütze hockt auf einer Straße"></div></div>

  <h1 class="front-title">DAS LICHT<br>AM UFER</h1>
  <p class="front-author">KONRAD(A) PELZMANN</p>

  <div class="spine-title">DAS LICHT AM UFER</div>
  <div class="spine-author">KONRADA PELZMANN</div>

  <p class="blurb blurb--main">Ein Leben beginnt nicht mit großen Worten, sondern mit kleinen Momenten. Dieses Buch erzählt von einer Kindheit in einer stillen Stadt, von ersten Fahrten auf dem Fahrrad, von Freundschaften, die blieben, und von Wegen, die sich trennten. Es erzählt von Arbeit und Zweifel, von Liebe und Verlust, von Jahren, in denen alles möglich schien, und von Tagen, an denen nichts gelingen wollte. Mit Ehrlichkeit und leisem Humor blickt der Autor zurück auf Stationen, Menschen und Orte, die ihn geprägt haben.<br>Entstanden ist ein Roman über Herkunft und Heimat, über Familie und Freundschaft, über Mut und Umwege und über das, was am Ende wirklich zählt. Zwischen den Zeilen liegen Sommerabende am Wasser, Briefe, die nie abgeschickt wurden, und Entscheidungen, die ein ganzes Leben verändert haben.</p>

  <p class="blurb blurb--closing">Geschrieben für die eigene Familie, für die Frau an seiner Seite und für die Söhne mit ihren Kindern, ist dieses Buch zugleich eine Einladung an alle Leser, innezuhalten. Denn jede Geschichte beginnt in der Zeit davor, und jede Erinnerung ist ein Stück Licht, das wir weitergeben, bevor es im Alltag verblasst. Ein stilles, warmes Buch über das Erinnern, über Dankbarkeit und über die leisen Dinge, die bleiben, wenn die lauten längst vergangen sind.</p>

  <div class="author-photo" role="img" aria-label="Autorenfoto: Mann mit grauem Haar im dunklen Anzug"></div>
  <div class="code-box">Konrad(a) Pelzmann.</div>
</div>
</body>
</html>
```